Brand New Solar Energy Business Needs a Flyer Design

We need an A5 double sided flyer for a new company in South Australia called Dorrit & Glow. We install home solar power systems and try to focus on quality of product and install.We also offer solar system servicing for existing systems which includes maintenance, cleaning and safety checks. Our web address is www.dorritandglow-example.com.au
We would like to see a design that's fresh and stands out in the mail box.
We feel the final design should communicate saving money on your electricity bills, local, quality and safety.
Target Market(s)
Home owners
Industry/Entity Type
Safety
Requirements
Must have
- A reference to our web site www.dorritandglow-example.com.au
A telephone number 0430000987

```html
<!DOCTYPE html>
<html lang="en">
<head>
<meta charset="utf-8">
<title>Dorrit &amp; Glow – Solar Flyer</title>
<link rel="stylesheet" href="https://fonts.googleapis.com/css2?family=Arimo:wght@400;700&family=Michroma&display=swap">
<style>
  :root{
    --white:#ffffff;
    --navy:#14215e;
    --navy-mid:#2a3f8f;
    --brand-blue:#2a8de0;
    --brand-green:#2f9a3a;
    --sky-top:#3d6fc4;
    --sky-low:#8fb3e2;
    --roof:#8a7566;
    --panel-blue:#2a4da3;
    --band-green:#2f9d3c;
    --band-blue:#1d9be0;
    --band-orange:#e8622a;
    --text-shadow:0 1px 3px rgba(0,0,0,.55);
  }
  *{margin:0;padding:0;box-sizing:border-box}
  html,body{width:1200px;height:822px;overflow:hidden;background:var(--white)}
  .flyer{position:relative;width:1200px;height:822px;overflow:hidden;font-family:"Arimo",Arial,sans-serif;color:var(--white)}

  /* front side */
  .front{position:absolute;left:0;top:0;width:600px;height:822px;background:var(--white)}
  .brand{position:absolute;left:138px;top:40px;display:flex;align-items:center;gap:10px}
  .brand-mark{width:74px;height:74px;border-radius:50%;background:var(--brand-green)}
  .brand-text{display:flex;flex-direction:column}
  .brand-name{font-family:"Arimo",Arial,sans-serif;font-weight:700;font-size:31px;color:var(--brand-blue);letter-spacing:.5px;line-height:1}
  .brand-tagline{font-size:10px;color:var(--brand-green);margin-top:4px;margin-left:40px}
  .front-photo{position:absolute;left:0;top:155px;width:600px;height:667px;
    background:linear-gradient(150deg,var(--sky-low) 0%,#c7d7ec 30%,var(--roof) 55%,#6b5a4f 100%)}
  .front-panel{position:absolute;left:0;top:155px;width:322px;height:667px;
    background:linear-gradient(180deg,var(--navy) 0%,var(--navy-mid) 45%,rgba(42,63,143,.75) 100%)}
  .headline{position:absolute;left:43px;top:200px;font-family:"Michroma",sans-serif;font-size:27px;line-height:31px;letter-spacing:1px;text-transform:uppercase;color:var(--white)}
  .benefits{position:absolute;left:44px;top:378px;width:262px;list-style:none;font-size:16px;line-height:20px;text-shadow:var(--text-shadow)}
  .benefits li{position:relative;padding-left:16px;margin-bottom:15px}
  .benefits li::before{content:"";position:absolute;left:0;top:8px;width:5px;height:5px;border-radius:50%;background:var(--white)}
  .web{position:absolute;left:44px;top:772px;font-size:10px;letter-spacing:.3px;color:var(--white)}

  /* back side */
  .back{position:absolute;left:600px;top:0;width:600px;height:822px;overflow:hidden}
  .back-photo{position:absolute;inset:0;
    background:linear-gradient(170deg,var(--sky-top) 0%,var(--sky-low) 40%,var(--panel-blue) 62%,#1e3a80 82%,#5a3a2c 100%)}
  .intro{position:absolute;left:57px;top:56px;width:260px;font-size:23px;line-height:27px;text-shadow:var(--text-shadow)}
  .intro p+p{margin-top:14px}
  .contact-bands{position:absolute;left:0;top:0;width:600px;height:822px;pointer-events:none}
  .band{position:absolute;height:30px;display:flex;align-items:center;padding-left:18px;
    font-family:"Michroma",sans-serif;font-size:10.5px;letter-spacing:.6px;color:var(--white);
    transform:rotate(-9deg);transform-origin:left center;white-space:nowrap}
  .band-green{left:105px;top:710px;width:560px;background:var(--band-green)}
  .band-blue{left:265px;top:730px;width:420px;background:var(--band-blue)}
  .band-orange{left:218px;top:790px;width:470px;background:var(--band-orange)}
</style>
</head>
<body>
<main class="flyer">
  <section class="front">
    <div class="brand">
      <span class="brand-mark"></span>
      <div class="brand-text">
        <span class="brand-name">Dorrit &amp; Glow</span>
        <span class="brand-tagline">Solar and Electrical Contractors</span>
      </div>
    </div>
    <div class="front-photo" role="img" aria-label="Smiling installer in safety harness kneeling on a shingled roof beside solar panels"></div>
    <div class="front-panel"></div>
    <h1 class="headline">Solar<br>solutions<br>for our<br>future<br>needs</h1>
    <ul class="benefits">
      <li>Save tonnes of greenhouse gas emissions.</li>
      <li>Free electricity with help from the sun.</li>
      <li>Affordable Premium solar solutions, tailored for you.</li>
      <li>Wipe out you electricity bills and protect against future electricity price rises.</li>
    </ul>
    <p class="web">www.dorritandglow-example.com.au</p>
  </section>

  <section class="back">
    <div class="back-photo" role="img" aria-label="Installer in hard hat and harness fitting solar panels on a roof under blue sky"></div>
    <div class="intro">
      <p>We install home solar power systems and try to focus on quality of product and installation.</p>
      <p>We also offer solar system servicing for existing systems which includes maintenance, cleaning and safety checks.</p>
    </div>
    <div class="contact-bands">
      <div class="band band-green">Contact Dorrit &amp; Glow today to discuss solar energy for you.</div>
      <div class="band band-blue">14 Wattle Lane, Harbourvale, SA 5999</div>
      <div class="band band-orange">Tel No.: 0430000987 | Fax: 08 7000 4412</div>
    </div>
  </section>
</main>
</body>
</html>
```